creation of a business card design for a company specializing in the creation...

I would like to create a design for a professional business card on a black background and with the company's colors (I am attaching some files: including the logo in horizontal and centered format, I am also attaching a recent project design a T-shirt, this is the one I chose to give you an idea of my preferences.

we are in the process of developing a new website design, it is still in the development phase but it can be viewed at the following address: www.vendrelak.be to give you other ideas about the company
you will see for yourself the subject of my main activity: company specializing in the construction of stairs

I would like a business card that stands out from the rest with a unique design

here is the informations
Name: Florent Dubrec
Function: Manager
Address: Rue Masquelin du Pont 41
7180 Val-Méroux
telephone: +32 486 219 508
email: info@rv8k.be
website: rv8k. be
social networks: Facebook, YouTube, TikTok, Instagram

Target Market(s)

customer who wants to have a beautiful staircase built

Industry/Entity Type

contruction d'escalier

Contact Information for Business Card

Adresse. Numero de telephone, site web, le texte : "Createur d'escalier", logo recto-verso, icone des reseaux sociaux

Requirements
Must have
• the mention: Stair creator
Nice to have
• an illustration of a designer staircase
Should not have
• do not distort the logo

```html
<!DOCTYPE html>
<html lang="fr">
<head>
<meta charset="utf-8">
<title>RV8K – Cartes de visite</title>
<link href="https://fonts.googleapis.com/css2?family=Montserrat:wght@400;500;700&family=Oswald:wght@600&display=swap" rel="stylesheet">
<style>
  :root{
    --bg:#3a3a3c;
    --card:#141415;
    --blue:#6f9cc0;
    --blue-deep:#2f5f7e;
    --white:#f2f2f2;
    --grey:#b9b9b9;
  }
  *{box-sizing:border-box;margin:0;padding:0}
  html,body{width:1200px;height:801px;overflow:hidden;background:var(--bg);font-family:"Montserrat",sans-serif}
  .stage{position:relative;width:1200px;height:801px;display:flex;align-items:center;justify-content:center;gap:40px}
  .card{position:relative;width:540px;height:340px;background:var(--card);border:1.5px solid var(--blue);box-shadow:0 18px 40px rgba(0,0,0,.45)}

  /* front */
  .divider{position:absolute;left:40px;right:40px;top:178px;height:1px;background:var(--blue)}
  .brand{position:absolute;right:40px;top:48px;display:flex;align-items:center;gap:14px}
  .brand-square{width:38px;height:38px;background:var(--blue)}
  .brand-text{display:flex;flex-direction:column;color:var(--white)}
  .brand-name{font-weight:500;font-size:38px;letter-spacing:3px;line-height:1}
  .brand-tag{font-size:7.5px;letter-spacing:3.4px;color:var(--grey);margin-top:4px}
  .person{position:absolute;left:40px;top:118px}
  .person-name{color:var(--blue);font-weight:700;font-size:22px;text-transform:uppercase;letter-spacing:.5px}
  .person-role{color:var(--white);font-size:14px;margin-top:4px}
  .contacts{position:absolute;left:40px;top:202px;list-style:none;color:var(--white);font-size:15px}
  .contacts li{display:flex;align-items:center;gap:10px;height:26px}
  .contacts svg{width:13px;height:13px;fill:var(--blue)}
  .address{position:absolute;right:40px;top:202px;text-align:right;color:var(--white);font-size:15px;line-height:1.6}

  /* back */
  .back{display:flex;flex-direction:column;align-items:center;padding-top:28px}
  .badge-title{font-family:"Oswald",sans-serif;font-weight:600;color:var(--white);font-size:20px;letter-spacing:1px;text-transform:uppercase}
  .badge-art{width:170px;height:120px;margin-top:6px;border-radius:50% 50% 12px 12px;background:radial-gradient(circle at 50% 40%,#8c8c8c 0%,var(--blue-deep) 55%,#1d3a4d 100%)}
  .back-name{color:var(--white);font-weight:500;font-size:46px;letter-spacing:6px;line-height:1;margin-top:10px}
  .back-tag{color:var(--blue);font-size:13px;letter-spacing:4.5px;margin-top:4px}
  .back-contact{display:flex;gap:14px;color:var(--white);font-size:11px;margin-top:8px;align-items:center}
  .back-contact span{display:flex;align-items:center;gap:5px}
  .dot{width:10px;height:10px;border-radius:50%;background:var(--blue)}
  .socials{display:flex;gap:8px;margin-top:8px}
  .socials i{width:13px;height:13px;border-radius:50%;background:var(--blue)}
</style>
</head>
<body>
<main class="stage">
  <section class="card front">
    <div class="brand">
      <div class="brand-square"></div>
      <div class="brand-text">
        <span class="brand-name">RV8K</span>
        <span class="brand-tag">ORIGINAL STAIRCASES</span>
      </div>
    </div>
    <div class="person">
      <p class="person-name">Florent Dubrec</p>
      <p class="person-role">Manager</p>
    </div>
    <div class="divider"></div>
    <ul class="contacts">
      <li><svg viewBox="0 0 24 24"><path d="M6.6 10.8a15 15 0 0 0 6.6 6.6l2.2-2.2c.3-.3.7-.4 1-.2 1.1.4 2.3.6 3.6.6.6 0 1 .4 1 1V20c0 .6-.4 1-1 1A17 17 0 0 1 3 4c0-.6.4-1 1-1h3.5c.6 0 1 .4 1 1 0 1.3.2 2.5.6 3.6.1.3 0 .7-.2 1z"/></svg>+32 486 219 508</li>
      <li><svg viewBox="0 0 24 24"><path d="M2 5h20v14H2zM4 7v.5l8 5 8-5V7l-8 5z"/></svg>info@rv8k.be</li>
      <li><svg viewBox="0 0 24 24"><circle cx="12" cy="12" r="10"/></svg>rv8k. be</li>
    </ul>
    <p class="address">Rue Masquelin du Pont 41<br>7180 Val-Méroux</p>
  </section>

  <section class="card back">
    <p class="badge-title">Créateur d'escalier</p>
    <div class="badge-art" role="img" aria-label="Illustration d'un escalier flottant dans un médaillon bleu"></div>
    <p class="back-name">RV8K</p>
    <p class="back-tag">ORIGINAL STAIRCASES</p>
    <div class="back-contact">
      <span><i class="dot"></i>0486 219 508</span>
      <span><i class="dot"></i>RV8K.BE</span>
    </div>
    <div class="socials" aria-label="Réseaux sociaux"><i></i><i></i><i></i><i></i></div>
  </section>
</main>
</body>
</html>
```